financial, economic news aggregation site, blog

Creation of a WordPress news blog, that will publish links to stories of relevant economic and financial news. Will include a picture with each link and the story headline. current examples with the type of look we are shooting for would include:
www.morningherald-example.net (good use of black as a contrast color, banner I provide may be black with reverse text)
www.brightledger-example.net (this is very good as it has a BIG feature story, some smaller headlines, some smaller thumbnails, and then another large feature underneath)
www.nightpost-example.net
www.gadgetloop-example.net
www.marketcorner-example.net (this one has a lots of variation in pic sizes, headlines, the site we are looking for does not need this much variation)

Target Market(s)

economic/financial news readers, policy professionals, people who follow politics

Coding

Coded - Design and coding required

Font styles to use
Sans Serif

Colors
0356a4
85acd3
ec1f27

Requirements
Must have
• - Slider featuring big stories or most recent stories
• - large thumbnail to accompany each news item, with headline and publication underneath
• - menu with categories (e.g. healthcare, tech, financial, regulation, environment, energy, opinion) etc. I will provide a "final" list after the initial draft is approved, if this is acceptable to the designer. Also since it is a WordPress site I will also assume that the menu can be customized - thank you.
• - social media icons, twitter, facebook (for now)
• Logo/banner header is attached -- this will be updated but please include as placeholder for now. IF the designer would like to
Nice to have
• place for widgets, such as a calculator for mortgage or car loan
Should not have
• can't think of anything

```html
<!DOCTYPE html>
<html lang="en">
<head>
<meta charset="utf-8">
<title>Civic Ledger News</title>
<link href="https://fonts.googleapis.com/css2?family=Roboto+Condensed:wght@700&family=Poppins:wght@400;500;600&display=swap" rel="stylesheet">
<style>
:root{
  --blue:#0356a4;
  --blue-bright:#1e62d0;
  --sky:#85acd3;
  --red:#ec1f27;
  --red-deep:#c8161e;
  --ink:#222;
  --muted:#777;
  --dark:#171717;
  --paper:#f4f4f4;
  --pink:#f9e3e4;
}
*{box-sizing:border-box;margin:0;padding:0}
html,body{width:1200px;height:5159px;overflow:hidden}
body{position:relative;font-family:"Poppins",sans-serif;color:var(--ink);background:#fff;font-size:14px}
.abs{position:absolute}
.photo{position:absolute;display:block}
.head-font{font-family:"Roboto Condensed",sans-serif;font-weight:700}

/* header */
.site-header{position:absolute;left:0;top:0;width:1200px;height:110px;background:var(--dark)}
.brand{position:absolute;left:140px;top:38px;color:#fff;font-family:"Poppins",sans-serif;font-weight:600;font-size:24px;line-height:30px;white-space:nowrap}
.brand-dot{display:inline-block;width:12px;height:12px;background:var(--red);border-radius:50%;margin-right:8px;vertical-align:middle}
.login{position:absolute;left:788px;top:30px;color:#fff;font-size:12px;font-weight:500}
.btn-subscribe{position:absolute;left:852px;top:24px;width:116px;height:28px;background:var(--blue-bright);color:#fff;font-size:12px;font-weight:500;text-align:center;line-height:28px;border-radius:2px}
.soc-circle{position:absolute;width:28px;height:28px;border:1.5px solid #fff;border-radius:50%}
.main-nav{position:absolute;top:76px;left:414px;display:flex;gap:20px;font-size:12px;font-weight:500;color:#fff;text-transform:uppercase;letter-spacing:.2px}
.main-nav .current{color:var(--red)}

/* hero */
.hero-img{left:0;top:110px;width:1200px;height:630px;background:linear-gradient(100deg,#0a2b52 0%,#0e4a8a 45%,#1a6fb5 70%,#0c2f5c 100%)}
.badge{position:absolute;top:272px;height:30px;color:#fff;font-size:11px;font-weight:600;line-height:30px;padding:0 14px;text-transform:uppercase}
.hero-title{position:absolute;left:142px;top:326px;color:#fff;font-size:54px;line-height:56px;text-transform:uppercase}
.hero-text{position:absolute;left:142px;top:450px;width:380px;color:#fff;font-size:16.5px;line-height:30px}
.arrow{position:absolute;top:384px;width:30px;height:30px;border-radius:50%;background:rgba(255,255,255,.85)}
.arrow svg{position:absolute;left:9px;top:8px}

/* section headings */
.sec-title{position:absolute;left:0;width:1200px;text-align:center;font-size:31px;color:#111;text-transform:uppercase}
.sec-mark{position:absolute;width:22px;height:16px}
.side-title{position:absolute;font-size:25px;color:#111;text-transform:uppercase;display:flex;align-items:center;gap:8px}

/* cards */
.card{position:absolute;background:#fff;box-shadow:0 2px 10px rgba(0,0,0,.12)}
.tag{position:absolute;background:var(--blue);color:#fff;font-size:10px;font-weight:600;padding:4px 12px;text-transform:uppercase}
.card-text{position:absolute;font-size:14px;line-height:24px;color:#333}
.meta{position:absolute;font-size:12.5px;color:#555;display:flex;align-items:center;gap:6px;white-space:nowrap}
.cal{display:inline-block;width:10px;height:10px;border:2px solid currentColor;border-top-width:3px;border-radius:1px}
.meta.blue{color:var(--blue)}
.meta.red{color:var(--red);font-style:italic}

/* grey zone */
.grey-zone{left:0;top:1900px;width:1200px;height:1375px;background:var(--paper)}
.story{position:absolute;left:132px;width:650px;height:222px;background:#fff;box-shadow:0 1px 6px rgba(0,0,0,.1)}
.story h3{position:absolute;left:312px;top:22px;width:300px;font-size:13.5px;font-weight:500;line-height:22px}
.story .meta{top:82px;left:312px;font-size:11.5px;gap:5px}
.story p{position:absolute;left:312px;top:114px;width:320px;font-size:10.5px;line-height:21px;color:#777}
.story .more{position:absolute;left:312px;top:186px;font-size:10px;font-weight:600;color:var(--blue)}

.calc{left:822px;top:2052px;width:246px;height:330px;background:var(--blue-bright);padding:20px 20px}
.calc label{display:block;color:#fff;font-size:13px;margin-bottom:8px}
.calc .field{background:#fff;height:38px;border:1px solid #ccc;font-size:12px;line-height:36px;padding-left:14px;margin-bottom:14px;color:#333}
.calc .btn{background:var(--red);color:#fff;text-align:center;font-size:15px;font-weight:600;height:32px;line-height:32px;text-transform:uppercase;border-radius:2px}

.latest{left:822px;top:2468px;width:246px;height:487px;background:#fff;box-shadow:0 1px 6px rgba(0,0,0,.1)}
.latest-item{position:absolute;left:16px;width:220px;height:88px}
.latest-item .photo{left:0;top:0;width:97px;height:86px}
.latest-item p{position:absolute;left:112px;top:2px;width:108px;font-size:13px;line-height:22px;white-space:nowrap;overflow:hidden}
.latest-item .meta{left:112px;top:70px;font-size:10.5px}

.tile{position:absolute;width:76px;height:73px;color:#fff;text-align:center;font-size:11px;line-height:14px;padding-top:14px}
.tile i{display:block;width:18px;height:18px;background:#fff;border-radius:50%;margin:0 auto 6px}

.fin-big{left:130px;top:2855px;width:305px;height:310px}
.fin-small{position:absolute;left:460px;width:322px;height:140px;background:#fff;box-shadow:0 1px 6px rgba(0,0,0,.1)}
.fin-small .photo{left:0;top:0;width:142px;height:140px}
.fin-small p{position:absolute;left:158px;top:26px;width:160px;font-size:12px;line-height:21px;white-space:nowrap}
.fin-small .meta{left:158px;top:98px;font-size:10.5px}

/* video */
.video-band{left:0;top:3275px;width:1200px;height:636px;background:linear-gradient(180deg,#e21d25 0%,#c3161d 70%,#a5121a 100%)}
.video-title{position:absolute;left:0;top:3364px;width:1200px;text-align:center;color:#fff;font-size:36px}
.video-item{position:absolute;left:726px;width:346px;height:98px;background:var(--pink)}
.video-item .photo{left:8px;top:8px;width:90px;height:82px}
.video-item p{position:absolute;left:114px;top:14px;width:210px;font-size:15px;line-height:24px;color:#222}
.video-item .meta{left:114px;top:70px;font-size:11.5px;gap:18px}

/* discussions */
.disc-card{position:absolute;top:4100px;width:306px;height:400px}
.disc-card h3{position:absolute;left:22px;top:218px;width:270px;font-size:17px;font-weight:500;line-height:26px}
.disc-card .meta{left:22px;top:282px}
.disc-card p{position:absolute;left:22px;top:312px;width:270px;font-size:12.5px;line-height:25px;color:#555}
.disc-item{position:absolute;left:817px;width:245px;height:110px;border-bottom:1px solid #ddd}
.disc-item .photo{left:0;top:0;width:106px;height:106px}
.disc-item p{position:absolute;left:124px;top:2px;width:124px;font-size:12px;line-height:21px;white-space:nowrap}
.disc-item .meta{left:124px;top:76px;font-size:10.5px}

/* footer */
.footer{left:0;top:4705px;width:1200px;height:454px;background:var(--dark);color:#fff}
.foot-brand{position:absolute;left:120px;top:4790px;color:#fff;font-weight:600;font-size:21px;line-height:30px;white-space:nowrap}
.foot-head{position:absolute;top:4768px;color:#fff;font-size:16px;text-transform:uppercase;letter-spacing:.3px}
.foot-news{position:absolute;left:340px;width:260px;height:70px}
.foot-news .photo{left:0;top:0;width:100px;height:70px}
.foot-news p{position:absolute;left:124px;top:4px;width:136px;font-size:12px;line-height:21px;color:#fff;white-space:nowrap}
.foot-news .meta{left:124px;top:52px;font-size:10.5px;color:var(--blue-bright)}
.foot-copy{position:absolute;left:652px;top:4834px;width:250px;font-size:11px;line-height:20px;color:#ddd}
.foot-input{position:absolute;left:652px;top:4906px;width:248px;height:38px;border-radius:19px;background:#fff;color:#777;font-size:11.5px;line-height:38px;padding-left:18px}
.foot-btn{position:absolute;left:652px;top:4958px;width:118px;height:36px;border-radius:18px;background:var(--blue-bright);color:#fff;font-size:12px;font-weight:600;line-height:36px;text-align:center}
.quick{position:absolute;left:948px;top:4815px;list-style:none;font-size:13.5px;line-height:29.5px;color:#eee}
.copyright{position:absolute;left:0;top:5088px;width:1200px;text-align:center;font-size:13.5px;color:#eee}
</style>
</head>
<body>

<header class="site-header">
  <div class="brand"><span class="brand-dot"></span>Civic Ledger News</div>
  <div class="login">LOGIN</div>
  <div class="btn-subscribe">SUBSCRIBE</div>
  <span class="soc-circle" style="left:990px;top:24px"></span>
  <span class="soc-circle" style="left:1026px;top:24px"></span>
  <nav class="main-nav">
    <span class="current">Home</span><span>Healthcare</span><span>Tech</span><span>Financial</span><span>Regulation</span><span>Environment</span><span>Energy</span><span>Opinion</span>
  </nav>
</header>

<div class="photo hero-img" role="img" aria-label="Hand holding a tablet with glowing finance and technology icons and charts"></div>
<div class="badge" style="left:144px;background:var(--blue-bright)">Jan 25, 2019</div>
<div class="badge" style="left:288px;background:var(--red)">2 Comments</div>
<h1 class="hero-title head-font">Civic<br>Ledger News</h1>
<p class="hero-text">Nemo enim ipsam voluptatem quia voluptas sit aspernatur aut odit aut fugit, sed quia consequuntur magni dolores eos qui ratione voluptatem sequi nesciunt.</p>
<div class="arrow" style="left:60px"><svg width="12" height="14"><path d="M9 2 3 7l6 5" fill="none" stroke="#222" stroke-width="2.5"/></svg></div>
<div class="arrow" style="left:1108px"><svg width="12" height="14"><path d="M3 2l6 5-6 5" fill="none" stroke="#222" stroke-width="2.5"/></svg></div>

<svg class="abs" style="left:0;top:650px" width="1200" height="100" viewBox="0 0 1200 100">
  <path d="M0 88 H300 C340 88 340 18 420 18 H780 C860 18 860 88 900 88 H1200 V100 H0Z" fill="#fff"/>
  <path d="M0 88 H300 C340 88 340 18 420 18" fill="none" stroke="var(--blue-bright)" stroke-width="12"/>
  <path d="M780 18 C860 18 860 88 900 88 H1200" fill="none" stroke="var(--blue-bright)" stroke-width="12"/>
  <path d="M330 50 C360 10 380 8 420 8 H780 C820 8 840 10 870 50" fill="none" stroke="var(--red)" stroke-width="10"/>
</svg>

<!-- most recent stories -->
<svg class="sec-mark" style="left:589px;top:745px" viewBox="0 0 22 16"><path d="M2 3h18M2 8h18M2 13h18" stroke="var(--red)" stroke-width="2.5"/><path d="M2 8h18" stroke="var(--blue)" stroke-width="2.5"/></svg>
<h2 class="sec-title head-font" style="top:770px">Most Recent Stories</h2>

<div class="card" style="left:132px;top:845px;width:286px;height:320px">
  <div class="photo" style="left:0;top:0;width:286px;height:195px;background:linear-gradient(135deg,#d9d4cc,#8a8a88)" role="img" aria-label="Stethoscope on a desk with papers"></div>
  <span class="tag" style="left:12px;top:184px">Healthcare</span>
  <p class="card-text" style="left:14px;top:216px;width:262px">Donec nec dolor fermentum, aluam lacus fermentum, elementum</p>
  <div class="meta" style="left:14px;top:278px"><i class="cal"></i>March 1st, 2019</div>
</div>
<div class="card" style="left:456px;top:845px;width:286px;height:320px">
  <div class="photo" style="left:0;top:0;width:286px;height:195px;background:linear-gradient(135deg,#c9b8a0,#3b3a3c)" role="img" aria-label="Person writing at a desk with charts"></div>
  <span class="tag" style="left:12px;top:184px">Tech</span>
  <p class="card-text" style="left:14px;top:216px;width:262px">Donec nec dolor fermentum, aluam lacus fermentum, elementum</p>
  <div class="meta" style="left:14px;top:278px"><i class="cal"></i>March 1st, 2019</div>
</div>
<div class="card" style="left:780px;top:845px;width:286px;height:320px">
  <div class="photo" style="left:0;top:0;width:286px;height:195px;background:linear-gradient(135deg,#e8e0d0,#4b4a46)" role="img" aria-label="Business team reviewing documents at a table"></div>
  <span class="tag" style="left:12px;top:184px">Financial</span>
  <p class="card-text" style="left:14px;top:216px;width:262px">Donec nec dolor fermentum, aluam lacus fermentum, elementum</p>
  <div class="meta" style="left:14px;top:278px"><i class="cal"></i>March 1st, 2019</div>
</div>

<!-- news featured -->
<svg class="sec-mark" style="left:589px;top:1238px" viewBox="0 0 22 16"><path d="M2 3h18M2 13h18" stroke="var(--red)" stroke-width="2.5"/><path d="M2 8h18" stroke="var(--blue)" stroke-width="2.5"/></svg>
<h2 class="sec-title head-font" style="top:1263px">News Featured</h2>

<div class="card" style="left:132px;top:1338px;width:486px;height:388px">
  <div class="photo" style="left:0;top:0;width:486px;height:272px;background:linear-gradient(135deg,#cfc6b8,#6e6a66)" role="img" aria-label="Laptop with a clock and financial reports on a desk"></div>
  <p class="card-text" style="left:18px;top:286px;width:456px;font-size:14px">Nemo enim ipsam voluptatem quia voluptas sit aspernatur aut odit aut fugit, sed quia consequuntur</p>
  <div class="meta" style="left:18px;top:348px"><i class="cal"></i>March 1st, 2019</div>
</div>
<div class="card" style="left:652px;top:1338px;width:402px;height:110px">
  <div class="photo" style="left:0;top:0;width:120px;height:110px;background:linear-gradient(135deg,#6f7b86,#2d3238)" role="img" aria-label="Colleagues discussing at a laptop"></div>
  <p class="card-text" style="left:138px;top:8px;width:260px">Donec nec dolor fermentum, aluam lacus fermentum, elementum</p>
  <div class="meta" style="left:138px;top:70px"><i class="cal"></i>March 1st, 2019 &nbsp; By Lena Hart</div>
</div>
<div class="card" style="left:652px;top:1478px;width:402px;height:110px">
  <div class="photo" style="left:0;top:0;width:120px;height:110px;background:linear-gradient(135deg,#4a6a8a,#1e2a36)" role="img" aria-label="Team in front of data screens"></div>
  <p class="card-text" style="left:138px;top:8px;width:260px">Donec nec dolor fermentum, aluam lacus fermentum, elementum</p>
  <div class="meta" style="left:138px;top:70px"><i class="cal"></i>March 1st, 2019 &nbsp; By Lena Hart</div>
</div>
<div class="card" style="left:652px;top:1616px;width:402px;height:110px">
  <div class="photo" style="left:0;top:0;width:120px;height:110px;background:linear-gradient(135deg,#d8d8d8,#6c6c6c)" role="img" aria-label="Bull and bear statues facing off"></div>
  <p class="card-text" style="left:138px;top:8px;width:260px">Donec nec dolor fermentum, aluam lacus fermentum, elementum</p>
  <div class="meta" style="left:138px;top:70px"><i class="cal"></i>March 1st, 2019 &nbsp; By Lena Hart</div>
</div>

<!-- grey zone -->
<div class="abs grey-zone"></div>
<svg class="abs" style="left:0;top:1835px" width="1200" height="90" viewBox="0 0 1200 90">
  <path d="M0 80 H300 C340 80 340 12 420 12 H780 C860 12 860 80 900 80 H1200 V90 H0Z" fill="var(--paper)"/>
  <path d="M0 80 H300 C340 80 340 16 420 16" fill="none" stroke="var(--blue-bright)" stroke-width="12"/>
  <path d="M780 16 C860 16 860 80 900 80 H1200" fill="none" stroke="var(--blue-bright)" stroke-width="12"/>
  <path d="M330 42 C360 6 380 6 420 6 H780 C820 6 840 6 870 42" fill="none" stroke="var(--red)" stroke-width="10"/>
</svg>

<h2 class="side-title head-font" style="left:130px;top:1988px"><svg width="26" height="16"><path d="M1 3h24M1 13h24" stroke="var(--red)" stroke-width="2.5"/><path d="M1 8h24" stroke="var(--blue)" stroke-width="2.5"/></svg>News Top Story</h2>
<h2 class="side-title head-font" style="left:822px;top:1988px"><svg width="26" height="16"><path d="M1 3h24M1 13h24" stroke="var(--red)" stroke-width="2.5"/><path d="M1 8h24" stroke="var(--blue)" stroke-width="2.5"/></svg>Calculator</h2>

<article class="story" style="top:2050px">
  <div class="photo" style="left:0;top:0;width:286px;height:222px;background:linear-gradient(135deg,#8a7a6a,#3a3530)" role="img" aria-label="Business people meeting in an office"></div>
  <h3>Nemo enim ipsam voluptatem quia voluptas sit aspernatur</h3>
  <div class="meta blue"><i class="cal"></i>Jan 25, 2019 &nbsp;&nbsp;&nbsp; 2 comments &nbsp;&nbsp;&nbsp; by Owen Reyes</div>
  <p>Sed ut perspiciatis unde omnis iste natus error sit voluptatem accusantium doloremque laudantium, totam rem aperiam, eaque ipsa quae ab illo inventore veritatis</p>
  <span class="more">READ MORE &gt;&gt;</span>
</article>
<article class="story" style="top:2290px">
  <div class="photo" style="left:0;top:0;width:286px;height:222px;background:linear-gradient(135deg,#5a82a8,#27384a)" role="img" aria-label="Professionals in front of glowing data screens"></div>
  <h3>Nemo enim ipsam voluptatem quia voluptas sit aspernatur</h3>
  <div class="meta blue"><i class="cal"></i>Jan 25, 2019 &nbsp;&nbsp;&nbsp; 2 comments &nbsp;&nbsp;&nbsp; by Owen Reyes</div>
  <p>Sed ut perspiciatis unde omnis iste natus error sit voluptatem accusantium doloremque laudantium, totam rem aperiam, eaque ipsa quae ab illo inventore veritatis</p>
  <span class="more">READ MORE &gt;&gt;</span>
</article>
<article class="story" style="top:2530px">
  <div class="photo" style="left:0;top:0;width:286px;height:222px;background:linear-gradient(135deg,#d0c8bc,#5a5650)" role="img" aria-label="Hands analysing printed charts with a tablet"></div>
  <h3>Nemo enim ipsam voluptatem quia voluptas sit aspernatur</h3>
  <div class="meta blue"><i class="cal"></i>Jan 25, 2019 &nbsp;&nbsp;&nbsp; 2 comments &nbsp;&nbsp;&nbsp; by Owen Reyes</div>
  <p>Sed ut perspiciatis unde omnis iste natus error sit voluptatem accusantium doloremque laudantium, totam rem aperiam, eaque ipsa quae ab illo inventore veritatis</p>
  <span class="more">READ MORE &gt;&gt;</span>
</article>

<form class="abs calc">
  <label>Mortgage Amount $</label>
  <div class="field">175,000</div>
  <label>Mortgage Term</label>
  <div style="display:flex;gap:8px"><div class="field" style="width:126px">350</div><div class="field" style="width:72px;padding-left:10px">years ⇕</div></div>
  <label>Interest Rate %</label>
  <div class="field">0.1250</div>
  <div class="btn">Calculator</div>
</form>

<h2 class="side-title head-font" style="left:822px;top:2412px"><svg width="26" height="16"><path d="M1 3h24M1 13h24" stroke="var(--red)" stroke-width="2.5"/><path d="M1 8h24" stroke="var(--blue)" stroke-width="2.5"/></svg>Latest News</h2>
<div class="abs latest">
  <div class="latest-item" style="top:24px"><div class="photo" style="background:linear-gradient(135deg,#2b5f8a,#0f2030)" role="img" aria-label="Globe with network lines"></div><p>Nemo enim<br>ipsam volupta<br>voluptas sit</p><div class="meta blue"><i class="cal"></i>Jan 25, 2019</div></div>
  <div class="latest-item" style="top:140px"><div class="photo" style="background:linear-gradient(135deg,#8a6a50,#3a2a20)" role="img" aria-label="Smiling professional in an office"></div><p>Nemo enim<br>ipsam volupta<br>voluptas sit</p><div class="meta blue"><i class="cal"></i>Jan 25, 2019</div></div>
  <div class="latest-item" style="top:256px"><div class="photo" style="background:linear-gradient(135deg,#7ab85a,#2a4a20)" role="img" aria-label="Green eco technology icons"></div><p>Nemo enim<br>ipsam volupta<br>voluptas sit</p><div class="meta blue"><i class="cal"></i>Jan 25, 2019</div></div>
  <div class="latest-item" style="top:372px"><div class="photo" style="background:linear-gradient(135deg,#a0968a,#3c3834)" role="img" aria-label="Person working on a laptop"></div><p>Nemo enim<br>ipsam volupta<br>voluptas sit</p><div class="meta blue"><i class="cal"></i>Jan 25, 2019</div></div>
</div>

<div class="tile" style="left:822px;top:2987px;background:#3b5998"><i></i>68,876<br>Fans</div>
<div class="tile" style="left:906px;top:2987px;background:#2fa8e6"><i></i>65<br>Followers</div>
<div class="tile" style="left:990px;top:2987px;background:#d62b2b"><i></i>8,961<br>Followers</div>
<div class="tile" style="left:822px;top:3072px;background:#1d78b5"><i></i>68,876<br>Fans</div>
<div class="tile" style="left:906px;top:3072px;background:#d42a22"><i></i>65<br>Followers</div>
<div class="tile" style="left:990px;top:3072px;background:#3c6fd4"><i></i>8,961<br>Followers</div>

<h2 class="side-title head-font" style="left:130px;top:2796px"><svg width="26" height="16"><path d="M1 3h24M1 13h24" stroke="var(--red)" stroke-width="2.5"/><path d="M1 8h24" stroke="var(--blue)" stroke-width="2.5"/></svg>&nbsp;Financial News</h2>
<div class="card fin-big">
  <div class="photo" style="left:0;top:0;width:305px;height:195px;background:linear-gradient(135deg,#e0dbd2,#7c7670)" role="img" aria-label="Team meeting in a bright office"></div>
  <p class="card-text" style="left:22px;top:212px;width:270px;font-size:16px;line-height:26px">Sed ut perspiciatis unde omnis iste natus sit voluptatem</p>
  <div class="meta blue" style="left:22px;top:274px;font-size:12px"><i class="cal"></i>March 1st, 2019 &nbsp;| &nbsp;Rita Vance</div>
</div>
<div class="fin-small" style="top:2855px">
  <div class="photo" style="background:linear-gradient(135deg,#3a5a8a,#0f1a2a)" role="img" aria-label="Businessman overlooking a city skyline"></div>
  <p>Lorem ipsum dolor sit<br>amet, consectetur adiing<br>elit, sed do eiusmod</p>
  <div class="meta blue"><i class="cal"></i>Jan 25, 2019</div>
</div>
<div class="fin-small" style="top:3020px">
  <div class="photo" style="background:linear-gradient(135deg,#6aa0c8,#1a2a40)" role="img" aria-label="Hands with a tablet projecting city data"></div>
  <p>Lorem ipsum dolor sit<br>amet, consectetur adiing<br>elit, sed do eiusmod</p>
  <div class="meta blue"><i class="cal"></i>Jan 25, 2019</div>
</div>

<!-- video -->
<div class="abs video-band"></div>
<svg class="sec-mark" style="left:589px;top:3342px" viewBox="0 0 22 16"><path d="M2 3h18M2 8h18M2 13h18" stroke="#fff" stroke-width="2.5"/></svg>
<h2 class="video-title head-font">Civic Ledger Video News</h2>
<div class="photo" style="left:134px;top:3468px;width:564px;height:332px;background:linear-gradient(100deg,#1a2438 0%,#3a3a40 45%,#c8a050 75%,#6a5030 100%)" role="img" aria-label="Stacks of coins before a city skyline at sunset"></div>
<svg class="abs" style="left:392px;top:3608px" width="48" height="48"><circle cx="24" cy="24" r="21" fill="none" stroke="#fff" stroke-width="2"/><path d="M19 15v18l14-9z" fill="#fff"/></svg>
<div class="video-item" style="top:3470px"><div class="photo" style="background:linear-gradient(135deg,#8a8a90,#2a2a30)" role="img" aria-label="Businessman talking on the phone"></div><p>Nemo enim ipsam volupta quia voluptas</p><div class="meta red"><i class="cal"></i>Jan 25, 2019 <span>2 comments</span></div></div>
<div class="video-item" style="top:3586px"><div class="photo" style="background:linear-gradient(135deg,#9a8a7a,#30282a)" role="img" aria-label="Colleagues in a meeting room"></div><p>Nemo enim ipsam volupta quia voluptas</p><div class="meta red"><i class="cal"></i>Jan 25, 2019 <span>2 comments</span></div></div>
<div class="video-item" style="top:3702px"><div class="photo" style="background:linear-gradient(135deg,#a0a4a8,#3a3c40)" role="img" aria-label="Professional on a phone call"></div><p>Nemo enim ipsam volupta quia voluptas</p><div class="meta red"><i class="cal"></i>Jan 25, 2019 <span>2 comments</span></div></div>

<!-- discussions -->
<svg class="sec-mark" style="left:589px;top:3978px" viewBox="0 0 22 16"><path d="M2 3h18M2 13h18" stroke="var(--red)" stroke-width="2.5"/><path d="M2 8h18" stroke="var(--blue)" stroke-width="2.5"/></svg>
<h2 class="sec-title head-font" style="top:4003px">Discussions Latest</h2>

<article class="card disc-card" style="left:127px">
  <div class="photo" style="left:0;top:0;width:306px;height:195px;background:linear-gradient(135deg,#c8bca8,#5a5248)" role="img" aria-label="Hands using a tablet with charts"></div>
  <h3>Sed ut perspiciatis unde omnis iste natus sit voluptatem</h3>
  <div class="meta blue"><i class="cal"></i>March 1st, 2019</div>
  <p>Lorem ipsum dolor sit amet, consectetur adipiscing elit, sed do eiusmod tempor incididunt ut labore et dolore</p>
</article>
<article class="card disc-card" style="left:469px">
  <div class="photo" style="left:0;top:0;width:306px;height:195px;background:linear-gradient(135deg,#e0e0e0,#3a3a3a)" role="img" aria-label="Trader viewing stock charts on screens"></div>
  <h3>Sed ut perspiciatis unde omnis iste natus sit voluptatem</h3>
  <div class="meta blue"><i class="cal"></i>March 1st, 2019</div>
  <p>Lorem ipsum dolor sit amet, consectetur adipiscing elit, sed do eiusmod tempor incididunt ut labore et dolore</p>
</article>
<div class="disc-item" style="top:4100px"><div class="photo" style="background:linear-gradient(135deg,#b09070,#3a2a20)" role="img" aria-label="Person smiling in an office"></div><p>Duis aute irure dolor<br>in reprehenderit in<br>voluptate</p><div class="meta blue"><i class="cal"></i>Jan 25, 2019</div></div>
<div class="disc-item" style="top:4245px"><div class="photo" style="background:linear-gradient(135deg,#7a8a98,#2a3038)" role="img" aria-label="Colleagues talking together"></div><p>Duis aute irure dolor<br>in reprehenderit in<br>voluptate</p><div class="meta blue"><i class="cal"></i>Jan 25, 2019</div></div>
<div class="disc-item" style="top:4390px;border:0"><div class="photo" style="background:linear-gradient(135deg,#6a80a0,#1a2030)" role="img" aria-label="City skyline at dusk"></div><p>Duis aute irure dolor<br>in reprehenderit in<br>voluptate</p><div class="meta blue"><i class="cal"></i>Jan 25, 2019</div></div>

<!-- footer -->
<svg class="abs" style="left:0;top:4620px" width="1200" height="90" viewBox="0 0 1200 90">
  <path d="M0 80 H300 C340 80 340 12 420 12 H780 C860 12 860 80 900 80 H1200 V90 H0Z" fill="var(--dark)"/>
  <path d="M0 80 H300 C340 80 340 16 420 16" fill="none" stroke="var(--blue-bright)" stroke-width="12"/>
  <path d="M780 16 C860 16 860 80 900 80 H1200" fill="none" stroke="var(--blue-bright)" stroke-width="12"/>
  <path d="M330 42 C360 6 380 6 420 6 H780 C820 6 840 6 870 42" fill="none" stroke="var(--red)" stroke-width="10"/>
</svg>
<footer class="abs footer"></footer>
<div class="foot-brand"><span class="brand-dot"></span>Civic Ledger News</div>
<span class="soc-circle" style="left:120px;top:4852px;width:24px;height:24px"></span>
<span class="soc-circle" style="left:152px;top:4852px;width:24px;height:24px"></span>

<h3 class="foot-head head-font" style="left:340px">Even More News</h3>
<div class="foot-news" style="top:4852px"><div class="photo" style="background:linear-gradient(135deg,#4a7aa8,#1a2a40)" role="img" aria-label="Professionals in a modern office"></div><p>Duis aute irure dolor<br>in reprehenderit in</p><div class="meta"><i class="cal"></i>Jan 25, 2019</div></div>
<div class="foot-news" style="top:4940px"><div class="photo" style="background:linear-gradient(135deg,#c04050,#2a1020)" role="img" aria-label="Crowd at a business event"></div><p>Duis aute irure dolor<br>in reprehenderit in</p><div class="meta"><i class="cal"></i>Jan 25, 2019</div></div>

<h3 class="foot-head head-font" style="left:652px">Sign Up To Receive Email</h3>
<p class="foot-copy">Excepteur sint occaecat cupidatat non proident, sunt in culpa qui Nemo enim ipsam voluptatem</p>
<div class="foot-input">Enter Email</div>
<div class="foot-btn">SUBSCRIBE</div>

<h3 class="foot-head head-font" style="left:944px">Quick Links</h3>
<ul class="quick">
  <li>Advertise With Us</li><li>Contact Us</li><li>Privacy Policy</li><li>Terms of Use</li><li>Careers</li><li>Internships</li>
</ul>
<p class="copyright">Copyright © Civic Ledger News 2019. All rights reserved. | Privacy Policy</p>

</body>
</html>
```